Larch Tutoring needs a flyer design

We are a tutoring company based in Melbourne. We provide group tutoring, private tutoring and workshop for HSQ students. We are now seeking a flyer for our Study Sprint Sessions. We would like to see a neat and simple design contains essential information. Also the design should be targeting high school students and their parents. It should be eye-catching. Our tutors are 99.95 graduates(highest score achievers). This is also our strength.

Hi,

Thanks for showing interest.
The essential information should be time, location, and some details.

Time: 30/8, 6/9, 13/9, 20/9
Details: On every date, there are three groups, each contains 5 students and 1 tutors, for every subject. 10am-12, 12-2pm, 2-4pm are the session time for students to choose. Subjects are Chemistry, Maths Methods, Specialist Maths, Business Management, Further Maths and Biology.

Location is Harwick Reading Hall.(517 Pellinor Rd, Melbourne)

Our strength is that the tutors are 99.95 graduates, like full-marks obtainers. Notes are well designed by them to focus on BRQT exams.

Logo is on our web.

Contact detail: www.larchtutoring.example.au
contact@larchtutoring.example.au
www.friendspace/larchtutoring

Measurement should be B4 size.

The essential information should be time, location, and some details. Time: 30/8, 6/9, 13/9, 20/9 Details: On every date, there are three groups, each contains 5 students and 1 tutors, for every subject. 10am-12, 12-2pm, 2-4pm are the session time for students to choose. Subjects are Chemistry, Maths Methods, Specialist Maths, Business Management, Further Maths and Biology. Location is Harwick Reading Hall.(517 Pellinor Rd, Melbourne) Our strength is that the tutors are 99.95 graduates, like full-marks obtainers. Notes are well designed by them to focus on BRQT exams. Logo is on our web. Contact detail: www.larchtutoring.example.au contact@larchtutoring.example.au www.friendspace/larchtutoring Measurement should be B4 size. Cheers, Perrin

Target Market(s)

High school students and their parents

Industry/Entity Type

High School

Requirements
Must have
• Time: 30/8, 6/9, 13/9, 20/9

Logo is on our web.

Nice to have
• Eye-catching top lines.

```html
<!DOCTYPE html>
<html lang="en">
<head>
<meta charset="utf-8">
<title>Larch Tutoring – Study Sprint Sessions</title>
<link rel="stylesheet" href="https://fonts.googleapis.com/css2?family=Arimo:wght@400;700&display=swap">
<style>
  :root {
    --paper: #ffffff;
    --band-green: #b6e98a;
    --band-yellow: #f6f06a;
    --band-orange: #f7845f;
    --stripe-green: #b9ec93;
    --stripe-salmon: #f9a58a;
    --stripe-yellow: #f5f07a;
    --headline-red: #f0431e;
    --info-panel: #fdf7a6;
    --label-green: #8ee062;
    --bullet-red: #ee3b2a;
    --ink: #111111;
    --brand-orange: #f26a1b;
  }
  * { box-sizing: border-box; margin: 0; padding: 0; }
  html, body { width: 875px; height: 1200px; overflow: hidden; background: var(--paper); }
  .flyer {
    position: relative; width: 875px; height: 1200px; overflow: hidden;
    background: var(--paper); font-family: "Arimo", Arial, sans-serif; color: var(--ink);
  }
  .backdrop { position: absolute; inset: 0; }
  .brand-tile {
    position: absolute; left: 0; top: 0; width: 258px; height: 138px;
    background: var(--paper); display: flex; align-items: center; justify-content: center; gap: 10px;
  }
  .brand-dot { width: 22px; height: 22px; border-radius: 50%; background: var(--brand-orange); }
  .brand-name { font-size: 27px; font-weight: 700; color: var(--brand-orange); }
  .intro {
    position: absolute; left: 157px; top: 562px; width: 700px;
    text-align: center; color: var(--headline-red); font-variant: small-caps;
    font-size: 22px; line-height: 25.5px; letter-spacing: 0.8px; white-space: nowrap;
  }
  .info-panel {
    position: absolute; left: 214px; top: 692px; width: 530px; height: 200px;
    background: var(--info-panel); padding: 6px 0 0 51px;
  }
  .info-panel ul { list-style: none; }
  .info-panel li {
    position: relative; font-size: 18px; font-weight: 700; line-height: 23.5px;
    white-space: nowrap; letter-spacing: -0.1px;
  }
  .info-panel li::before {
    content: ""; position: absolute; left: -20px; top: 7px; width: 9px; height: 9px; background: var(--bullet-red);
  }
  .info-label { color: var(--label-green); text-decoration: underline; }
  .location {
    position: absolute; left: 248px; top: 898px; width: 500px;
    text-align: center; color: var(--headline-red); font-variant: small-caps;
    font-size: 22px; line-height: 25px; letter-spacing: 0.6px; white-space: nowrap;
  }
  .strength {
    position: absolute; left: 160px; top: 960px; width: 300px;
    font-variant: small-caps; font-size: 24px; line-height: 26.4px;
    letter-spacing: 0.6px; color: var(--ink); white-space: nowrap;
  }
  .contact {
    position: absolute; left: 464px; top: 1086px; width: 400px;
    text-align: center; font-size: 22px; line-height: 28px; color: var(--headline-red);
    white-space: nowrap;
  }
  .contact-title { color: var(--label-green); font-weight: 700; text-decoration: underline; }
</style>
</head>
<body>
<main class="flyer">
  <svg class="backdrop" width="875" height="1200" viewBox="0 0 875 1200">
    <defs>
      <linearGradient id="photoTone" x1="0" y1="0" x2="1" y2="1">
        <stop offset="0" stop-color="#6b5a4a"/>
        <stop offset="0.45" stop-color="#c9b8a6"/>
        <stop offset="1" stop-color="#e9e6e2"/>
      </linearGradient>
      <linearGradient id="fadeGreen" x1="0" y1="0" x2="0" y2="1">
        <stop offset="0" stop-color="var(--stripe-green)"/>
        <stop offset="0.75" stop-color="var(--stripe-green)"/>
        <stop offset="1" stop-color="#ffffff"/>
      </linearGradient>
      <linearGradient id="fadeSalmon" x1="0" y1="0" x2="0" y2="1">
        <stop offset="0" stop-color="var(--stripe-salmon)"/>
        <stop offset="0.75" stop-color="var(--stripe-salmon)"/>
        <stop offset="1" stop-color="#ffffff"/>
      </linearGradient>
      <linearGradient id="fadeYellow" x1="0" y1="0" x2="0" y2="1">
        <stop offset="0" stop-color="var(--stripe-yellow)"/>
        <stop offset="0.8" stop-color="var(--stripe-yellow)"/>
        <stop offset="1" stop-color="#ffffff"/>
      </linearGradient>
    </defs>
    <path role="img" aria-label="Photo of smiling students studying together around a laptop with a tutor"
          d="M0 0 H875 V505 C700 470 320 400 0 362 Z" fill="url(#photoTone)"/>
    <rect x="0" y="440" width="50" height="760" fill="url(#fadeGreen)"/>
    <rect x="50" y="455" width="74" height="745" fill="url(#fadeSalmon)"/>
    <rect x="126" y="470" width="16" height="730" fill="url(#fadeYellow)"/>
    <path d="M0 362 C320 400 700 470 875 505 L875 512 C640 500 300 470 0 455 Z" fill="var(--band-green)"/>
    <path d="M0 440 C300 462 640 495 875 512 L875 520 C620 515 280 492 0 470 Z" fill="var(--band-yellow)"/>
    <path d="M0 470 C280 492 620 515 875 520 L875 528 C600 528 270 515 0 500 Z" fill="var(--band-orange)"/>
  </svg>

  <div class="brand-tile">
    <span class="brand-dot"></span>
    <span class="brand-name">Larch Tutoring</span>
  </div>

  <p class="intro">Larch Ed Co. was founded in late 2013, and<br>further run by a group of outstanding HSQ high<br>achievers. We are dedicated to sharing our<br>knowledge and experience with students and<br>support them along the way.</p>

  <section class="info-panel">
    <ul>
      <li><span class="info-label">Time:</span> 30/8, 6/9, 13/9, 20/9</li>
      <li><span class="info-label">Details:</span> On every date, there are three groups,<br>each contains 5 students and 1 tutors, for<br>every subject. 10am-12, 12-2pm, 2-4pm are the<br>session time for students to choose. Subjects<br>are Chemistry, Maths Methods, Specialist<br>Maths, Business Management, Further Maths<br>and Biology.</li>
    </ul>
  </section>

  <p class="location">Location is Harwick Reading Hall.<br>(517 Pellinor Rd, Melbourne)</p>

  <p class="strength">Our strength is that<br>the tutors are 99.95<br>graduates, like full-<br>marks obtainers.<br>Notes are well<br>designed by them to<br>focus on BRQT exams</p>

  <section class="contact">
    <p class="contact-title">Contact detail:</p>
    <p>www.larchtutoring.example.au</p>
    <p>contact@larchtutoring.example.au</p>
    <p>www.friendspace/larchtutoring</p>
  </section>
</main>
</body>
</html>
```